Open Gate Chapel Outreach & 101.3 FM & 88.7 FM Radio

One side to be Open Gate Outreach logo (under design now) with Torvo & Maribel Quenstad contact info.

The other side to show Torvo Quenstad info and;

101.3 FM The LAMP
M-F 9:00pm-9:30pm
for the Broken, Lost & incarcerated

88.7 FM The DOVE
M-F 6:00am-10:00am
The Isles' only LIVE Christian Radio Program
Fun for the whole family!

Radio logos can be taken from websites

Industry/Entity Type

Radio

```html
<!DOCTYPE html>
<html lang="en">
<head>
<meta charset="utf-8">
<title>Open Gate Outreach – Business Card</title>
<link href="https://fonts.googleapis.com/css2?family=Arimo:wght@400;700&display=swap" rel="stylesheet">
<style>
  :root {
    --page: #e9eaec;
    --card-white: #ffffff;
    --ink-blue: #2f57b3;
    --title-blue: #5670c4;
    --band-blue: #4a73c6;
    --band-text: #ffffff;
    --name-ink: #3b4f8e;
    --rule: #8a94ad;
    --sky-deep: #7fa6dc;
    --sky-mid: #b9d0ee;
    --sky-light: #f4f8fd;
  }
  * { box-sizing: border-box; margin: 0; padding: 0; }
  html, body {
    width: 1200px; height: 900px; overflow: hidden;
    background: var(--page);
    font-family: "Arimo", Arial, sans-serif;
  }
  .sheet {
    width: 1200px; height: 900px;
    display: flex; flex-direction: column;
    align-items: center; justify-content: center; gap: 36px;
  }
  .card {
    position: relative;
    width: 700px; height: 400px;
    overflow: hidden;
    box-shadow: 0 6px 18px rgba(0,0,0,0.14);
  }

  /* Front side */
  .card--front { background: var(--card-white); }
  .sky {
    position: absolute; inset: 0;
    background:
      radial-gradient(circle at 22% 55%, rgba(255,255,255,0.95) 0, rgba(255,255,255,0.6) 12%, rgba(255,255,255,0) 32%),
      radial-gradient(ellipse at 80% 10%, var(--sky-light) 0, rgba(244,248,253,0) 45%),
      radial-gradient(ellipse at 15% 85%, var(--sky-light) 0, rgba(244,248,253,0) 40%),
      linear-gradient(165deg, var(--sky-deep) 0%, var(--sky-mid) 40%, var(--sky-light) 75%);
  }
  .front-identity {
    position: absolute; left: 200px; top: 60px; width: 470px;
    text-align: center;
  }
  .ministry-name {
    font-size: 46px; font-weight: 400; color: var(--title-blue);
    letter-spacing: 0.5px;
  }
  .leaders { margin: 22px auto 0; width: 280px; }
  .leaders-names {
    font-size: 19px; color: var(--name-ink);
    padding-bottom: 6px; border-bottom: 1px solid var(--rule);
  }
  .leaders-role { font-size: 17px; color: #333a4a; margin-top: 6px; }
  .contact-band {
    position: absolute; left: 0; right: 0; bottom: 0; height: 128px;
    background: var(--band-blue);
    color: var(--band-text);
    display: flex; flex-direction: column; justify-content: center;
    padding-left: 170px; gap: 14px;
    font-size: 18px;
  }
  .contact-line { display: flex; align-items: center; gap: 12px; }
  .contact-line svg { width: 20px; height: 20px; fill: var(--band-text); flex: none; }
  .divider { margin: 0 18px; }

  /* Back side */
  .card--back {
    background: var(--card-white);
    display: flex; flex-direction: column; align-items: center; justify-content: center;
    text-align: center; color: var(--ink-blue);
  }
  .station { font-size: 17px; line-height: 1.45; }
  .station-tag { font-size: 21px; font-weight: 700; line-height: 1.35; }
  .station-block + .station-block { margin-top: 22px; }
</style>
</head>
<body>
<main class="sheet">

  <section class="card card--front" aria-label="Front of business card">
    <div class="sky" role="img" aria-label="Bright blue sky with soft white clouds and sun glare"></div>
    <div class="front-identity">
      <h1 class="ministry-name">Open Gate Outreach</h1>
      <div class="leaders">
        <p class="leaders-names">Torvo &amp; Maribel Quenstad</p>
        <p class="leaders-role">Leaders</p>
      </div>
    </div>
    <div class="contact-band">
      <p class="contact-line">
        <svg viewBox="0 0 24 24" aria-hidden="true"><path d="M6.6 10.8a15.1 15.1 0 0 0 6.6 6.6l2.2-2.2a1 1 0 0 1 1-.25 11.4 11.4 0 0 0 3.6.57 1 1 0 0 1 1 1V20a1 1 0 0 1-1 1A17 17 0 0 1 3 4a1 1 0 0 1 1-1h3.5a1 1 0 0 1 1 1c0 1.25.2 2.45.57 3.57a1 1 0 0 1-.25 1z"/></svg>
        <span>Torvo: 808.555.0142</span><span class="divider">|</span><span>Maribel: 808.555.0187</span>
      </p>
      <p class="contact-line">
        <svg viewBox="0 0 24 24" aria-hidden="true"><path d="M2 5h20v14H2z M2 5l10 8 10-8" fill="none" stroke="#fff" stroke-width="2"/></svg>
        <span>opengateoutreach@example.com</span>
      </p>
    </div>
  </section>

  <section class="card card--back" aria-label="Back of business card">
    <div class="station-block">
      <p class="station">101.3 FM The LAMP</p>
      <p class="station">M-F 9:00pm-9:30pm</p>
      <p class="station-tag">for the Broken, Lost &amp; Incarcerated</p>
    </div>
    <div class="station-block">
      <p class="station">88.7 FM The DOVE</p>
      <p class="station">M-F 6:00am-10:00am</p>
      <p class="station-tag">The Isles' only LIVE Christian Radio Program</p>
      <p class="station-tag">Fun for the whole family!</p>
    </div>
  </section>

</main>
</body>
</html>
```